Formal letterhead for Commercial Real Estate Company

Formal and professional letterhead for the transactional documents of a commercial real estate company.

Elements to be Included between header and footer:

- Logo (attached)(should be applied without the yellow background, in other words, the background colour for the design should be white)
- Slogan: Your Property Solution
- Physical Address: 27 Kestrel Lane, Ferndale, Durban, 4001
- Postal Address: PO Box 61894, Windermere, 4062
- Phone: 031 486 9142
- Fax: 031 337 8129
- Website: www.terrabuild.co.zaz
- eMail: contact@terrabuild.co.za

The brand guide is attached (the one you last provided), it does not provide direction on letterhead specifically but on other brand aspects.

Industry/Entity Type

Real Estate

```html
<!DOCTYPE html>
<html lang="en">
<head>
<meta charset="utf-8">
<title>Terrabuild Letterhead</title>
<link href="https://fonts.googleapis.com/css2?family=Open+Sans:wght@400;700;800&display=swap" rel="stylesheet">
<style>
  :root {
    --backdrop: #9a9a9a;
    --paper-top: #ffffff;
    --paper-bottom: #e6e6e6;
    --footer-band: #cfcfcf;
    --ink: #1a1a1a;
    --ink-soft: #3a3a3a;
  }
  html, body {
    margin: 0;
    padding: 0;
    width: 1079px;
    height: 1200px;
    overflow: hidden;
    background: var(--backdrop);
    font-family: "Open Sans", Arial, sans-serif;
  }
  .letterhead {
    position: absolute;
    left: 120px;
    top: 50px;
    width: 778px;
    height: 1100px;
    background: linear-gradient(to bottom, var(--paper-top) 0%, var(--paper-top) 30%, var(--paper-bottom) 100%);
    box-shadow: 0 6px 18px rgba(0,0,0,0.25);
  }
  .brand {
    position: absolute;
    top: 70px;
    left: 0;
    right: 0;
    display: flex;
    justify-content: center;
    align-items: center;
    gap: 10px;
  }
  .brand-square {
    width: 26px;
    height: 26px;
    background: var(--ink);
  }
  .brand-name {
    font-weight: 800;
    font-size: 30px;
    letter-spacing: 1px;
    color: var(--ink);
  }
  .footer {
    position: absolute;
    left: 0;
    right: 0;
    bottom: 0;
    height: 250px;
    background: var(--footer-band);
    text-align: center;
    color: var(--ink-soft);
  }
  .slogan {
    margin: 70px 0 0;
    font-weight: 700;
    font-size: 13px;
    letter-spacing: 6px;
    text-transform: uppercase;
    color: var(--ink);
  }
  .address {
    margin: 28px 0 0;
    font-size: 13px;
  }
  .contacts {
    margin: 6px 0 0;
    font-size: 13px;
    display: flex;
    justify-content: center;
    align-items: center;
    gap: 6px;
  }
  .contact-item {
    display: inline-flex;
    align-items: center;
    gap: 4px;
  }
  .contact-item svg {
    width: 11px;
    height: 11px;
    fill: var(--ink-soft);
  }
</style>
</head>
<body>
  <main class="letterhead">
    <header class="brand">
      <span class="brand-square"></span>
      <span class="brand-name">TERRABUILD</span>
    </header>

    <footer class="footer">
      <p class="slogan">Your Property Solution</p>
      <p class="address">27 Kestrel Lane, Ferndale, Durban, 4001 | PO Box 61894, Windermere, 4062</p>
      <p class="contacts">
        <span class="contact-item">
          <svg viewBox="0 0 24 24"><path d="M6.6 10.8a15 15 0 0 0 6.6 6.6l2.2-2.2c.3-.3.7-.4 1-.2 1.1.4 2.3.6 3.6.6.6 0 1 .4 1 1V20c0 .6-.4 1-1 1A17 17 0 0 1 3 4c0-.6.4-1 1-1h3.5c.6 0 1 .4 1 1 0 1.3.2 2.5.6 3.6.1.3 0 .7-.2 1z"/></svg>
          031 486 9142
        </span>|
        <span class="contact-item">
          <svg viewBox="0 0 24 24"><rect x="6" y="2" width="12" height="6"/><rect x="2" y="9" width="20" height="9" rx="2"/><rect x="6" y="15" width="12" height="7"/></svg>
          031 337 8129
        </span>|
        <span class="contact-item">
          <svg viewBox="0 0 24 24"><path d="M2 5h20v14H2z M2 5l10 8 10-8" fill="none" stroke="#3a3a3a" stroke-width="2.5"/></svg>
          contact@terrabuild.co.za
        </span>|
        <span class="contact-item">
          <svg viewBox="0 0 24 24"><circle cx="12" cy="12" r="9" fill="none" stroke="#3a3a3a" stroke-width="2.5"/><path d="M3 12h18M12 3c3 3 3 15 0 18M12 3c-3 3-3 15 0 18" fill="none" stroke="#3a3a3a" stroke-width="2"/></svg>
          www.terrabuild.co.zaz
        </span>
      </p>
    </footer>
  </main>
</body>
</html>
```